Wendale Ridge Concrete Pumping needs a logo design and is in the concrete industry

A creative design for this Wendale Ridge Concrete Pumping business. Using a trailer mounted line pump, not a boom pump.
Colour to be used is orange and a mix of white or black writing.
Target Market(s)
General Public, anyone
Industry/Entity Type
Concrete
Contact Information for Business Card
Wendale Ridge Concrete Pumping
Callum Hesketh
PO BOX 47
Marrindale Vic 3266
Phone: 0417952803
Email: Hesketh@bluewrenmail.com.au
Colors
f37122
000000
ffffff
Requirements
Must have
- Details listed
Nice to have
- A great logo
Should not have
- anything silly

```html
<!DOCTYPE html>
<html lang="en">
<head>
<meta charset="utf-8">
<title>Wendale Ridge Concrete Pumping – Business Card</title>
<link rel="stylesheet" href="https://fonts.googleapis.com/css2?family=Poppins:wght@600&display=swap">
<style>
  :root {
    --orange: #f7941d;
    --orange-deep: #d9780c;
    --black: #000000;
    --white: #ffffff;
    --backdrop: #e6e6e4;
    --card-shadow: rgba(0, 0, 0, 0.18);
  }
  * { margin: 0; padding: 0; box-sizing: border-box; }
  html, body {
    width: 1200px;
    height: 1147px;
    overflow: hidden;
    background: var(--backdrop);
    font-family: "Poppins", sans-serif;
    font-weight: 600;
  }
  .stage {
    position: relative;
    width: 1200px;
    height: 1147px;
  }
  .card {
    position: absolute;
    left: 180px;
    width: 840px;
    height: 480px;
    overflow: hidden;
    background: var(--orange);
    box-shadow: 0 6px 18px var(--card-shadow);
  }
  .card--front { top: 70px; }
  .card--back  { top: 597px; }

  .front-top {
    position: absolute;
    left: 0; top: 0;
    width: 100%;
    height: 62%;
    background: var(--black);
  }
  .back-top {
    position: absolute;
    left: 0; top: 0;
    width: 100%;
    height: 44%;
    background: var(--white);
  }

  .brand {
    position: absolute;
    color: var(--orange);
    line-height: 1.02;
    letter-spacing: -0.5px;
    white-space: nowrap;
  }
  .brand-mark {
    display: inline-block;
    background: var(--orange);
    vertical-align: middle;
  }
  .card--front .brand {
    left: 64px;
    top: 60px;
    font-size: 60px;
  }
  .card--front .brand-mark { width: 28px; height: 28px; margin-right: 14px; }
  .card--back .brand {
    left: 230px;
    top: 52px;
    font-size: 38px;
  }
  .card--back .brand-mark { width: 20px; height: 20px; margin-right: 12px; }

  .pump-operator {
    position: absolute;
    background: linear-gradient(180deg, var(--orange) 0%, var(--orange-deep) 100%);
  }
  .card--front .pump-operator {
    left: 700px;
    top: 70px;
    width: 100px;
    height: 300px;
  }
  .card--back .pump-operator {
    left: 640px;
    top: 30px;
    width: 60px;
    height: 170px;
  }

  .contact {
    position: absolute;
    left: 64px;
    top: 228px;
    color: var(--white);
  }
  .contact-name {
    font-size: 44px;
    line-height: 1.1;
    margin-bottom: 14px;
    letter-spacing: -0.5px;
  }
  .contact-lines {
    list-style: none;
    font-size: 26px;
    line-height: 1.36;
  }
</style>
</head>
<body>
  <main class="stage">
    <section class="card card--front" aria-label="Business card front">
      <div class="front-top"></div>
      <div class="brand">
        <span class="brand-mark"></span>Wendale Ridge<br>Concrete Pumping
      </div>
      <div class="pump-operator" role="img" aria-label="Illustration of a worker guiding a concrete pump hose"></div>
    </section>

    <section class="card card--back" aria-label="Business card back">
      <div class="back-top"></div>
      <div class="brand">
        <span class="brand-mark"></span>Wendale Ridge<br>Concrete Pumping
      </div>
      <div class="pump-operator" role="img" aria-label="Illustration of a worker guiding a concrete pump hose"></div>
      <div class="contact">
        <h1 class="contact-name">Callum Hesketh</h1>
        <ul class="contact-lines">
          <li>Po Box 47</li>
          <li>Marrindale Vic 3266</li>
          <li>Phone: 0417952803</li>
          <li>Email: Hesketh@bluewrenmail.com.au</li>
        </ul>
      </div>
    </section>
  </main>
</body>
</html>
```